Playing Card Box Deisgn

Quick video of what we're looking for in this design:

https://share.clipnook.com/watch/r2KTP48mdqHxzbnu7LWyPe?

Here's our company website:
https://mybrambletoys.com/

Attached is the file of what we have so far for this box design. Feel free to add or make other design suggestions

```html
<!DOCTYPE html>
<html lang="en">
<head>
<meta charset="utf-8">
<title>Playing Card Box Dieline</title>
<link rel="stylesheet" href="https://fonts.googleapis.com/css2?family=Montserrat:wght@300;400;600;700&display=swap">
<style>
  :root{
    --paper:#ffffff;
    --ink:#231f20;
    --bleed:#3b3fa0;
    --die:#e0218a;
    --safe:#1aa64a;
    --label:#333333;
    --white:#ffffff;
    --frame:#2ecc8f;
    --red:#e8312f;
    --green:#5cb85c;
    --gold:#f5b21b;
    --blue:#3f67c9;
    --purple:#7b4fb8;
    --pink:#e8447a;
  }
  html,body{margin:0;padding:0;overflow:hidden;background:var(--paper);}
  .sheet{width:1200px;height:904px;position:relative;overflow:hidden;background:var(--paper);}
  .sheet svg{position:absolute;left:0;top:0;width:1200px;height:904px;}
  .legend-label{font-family:'Montserrat',sans-serif;font-weight:300;font-size:28px;}
  .spec-label{font-family:'Montserrat',sans-serif;font-weight:300;font-size:28px;fill:var(--label);}
  .card-index{font-family:'Montserrat',sans-serif;font-weight:400;font-size:52px;fill:var(--white);}
  .brand-spine{font-family:'Montserrat',sans-serif;font-weight:600;font-size:22px;letter-spacing:5px;fill:var(--white);}
  .brand-front{font-family:'Montserrat',sans-serif;font-weight:700;font-size:50px;fill:var(--white);}
  .front-sub{font-family:'Montserrat',sans-serif;font-weight:600;font-size:20px;letter-spacing:3px;fill:var(--white);}
  .site-url{font-family:'Montserrat',sans-serif;font-weight:400;font-size:13px;letter-spacing:1px;fill:var(--white);}
  .die{fill:none;stroke:var(--die);stroke-width:1.2;}
  .safe{fill:none;stroke:var(--safe);stroke-width:1;stroke-dasharray:5 4;}
</style>
</head>
<body>
<div class="sheet">
<svg viewBox="0 0 2200 1657" preserveAspectRatio="none" xmlns="http://www.w3.org/2000/svg">
  <defs>
    <linearGradient id="jackArt" x1="0" y1="0" x2="1" y2="1">
      <stop offset="0" stop-color="#3f67c9"/><stop offset="0.5" stop-color="#f5b21b"/><stop offset="1" stop-color="#2ea37a"/>
    </linearGradient>
    <linearGradient id="queenArt" x1="0" y1="0" x2="1" y2="1">
      <stop offset="0" stop-color="#f5b21b"/><stop offset="0.5" stop-color="#3f67c9"/><stop offset="1" stop-color="#8cc63f"/>
    </linearGradient>
    <radialGradient id="backPattern" cx="0.5" cy="0.5" r="0.6">
      <stop offset="0" stop-color="#3a3536"/><stop offset="1" stop-color="#231f20"/>
    </radialGradient>
  </defs>

  <!-- legend -->
  <g class="legend">
    <text class="legend-label" x="218" y="202" text-anchor="end" fill="var(--bleed)">bleedline</text>
    <line x1="240" y1="194" x2="460" y2="194" stroke="var(--bleed)" stroke-width="1.2"/>
    <text class="legend-label" x="218" y="254" text-anchor="end" fill="var(--die)">dieline</text>
    <line x1="240" y1="250" x2="460" y2="250" stroke="var(--die)" stroke-width="1.2"/>
    <text class="legend-label" x="218" y="306" text-anchor="end" fill="var(--safe)">safeline</text>
    <line x1="240" y1="302" x2="460" y2="302" stroke="var(--safe)" stroke-width="1.5" stroke-dasharray="3 3"/>
  </g>

  <text class="spec-label" x="216" y="438">card：63x88mm</text>
  <text class="spec-label" x="1212" y="438">65x90x18mm</text>

  <!-- card: jack -->
  <g class="card card-jack">
    <rect x="109" y="535" width="379" height="517" fill="var(--ink)" stroke="var(--bleed)" stroke-width="1.2"/>
    <rect class="die" x="125" y="552" width="346" height="483" rx="20"/>
    <rect class="safe" x="142" y="570" width="313" height="448" rx="14"/>
    <text class="card-index" x="167" y="630" text-anchor="middle">J</text>
    <circle cx="167" cy="643" r="5" fill="var(--green)"/><circle cx="161" cy="652" r="5" fill="var(--green)"/><circle cx="173" cy="652" r="5" fill="var(--green)"/>
    <rect x="192" y="620" width="212" height="347" fill="url(#jackArt)" stroke="#888" stroke-width="1" role="img" aria-label="Court illustration of the jack of clubs"/>
    <g transform="rotate(180 430 960)">
      <text class="card-index" x="430" y="963" text-anchor="middle">J</text>
      <circle cx="430" cy="976" r="5" fill="var(--green)"/><circle cx="424" cy="985" r="5" fill="var(--green)"/><circle cx="436" cy="985" r="5" fill="var(--green)"/>
    </g>
  </g>

  <!-- card: queen -->
  <g class="card card-queen">
    <rect x="519" y="535" width="379" height="517" fill="var(--ink)" stroke="var(--bleed)" stroke-width="1.2"/>
    <rect class="die" x="535" y="552" width="346" height="483" rx="20"/>
    <rect class="safe" x="552" y="570" width="313" height="448" rx="14"/>
    <text class="card-index" x="577" y="630" text-anchor="middle">Q</text>
    <circle cx="577" cy="643" r="5" fill="var(--green)"/><circle cx="571" cy="652" r="5" fill="var(--green)"/><circle cx="583" cy="652" r="5" fill="var(--green)"/>
    <rect x="602" y="620" width="212" height="347" fill="url(#queenArt)" stroke="#888" stroke-width="1" role="img" aria-label="Court illustration of the queen of clubs"/>
    <g transform="rotate(180 841 960)">
      <text class="card-index" x="841" y="963" text-anchor="middle">Q</text>
      <circle cx="841" cy="976" r="5" fill="var(--green)"/><circle cx="835" cy="985" r="5" fill="var(--green)"/><circle cx="847" cy="985" r="5" fill="var(--green)"/>
    </g>
  </g>

  <!-- tuck box dieline -->
  <g class="tuck-box">
    <path fill="var(--ink)" d="M1042,1335 L1042,718 L1060,700 L1075,643 L1140,643 L1140,608 C1140,490 1527,490 1527,608 L1527,643 L1595,643 L1610,700 L1628,718 L1965,725 L2057,758 L2057,1220 L1980,1248 L1980,1370 C1980,1488 1595,1488 1595,1370 L1595,1335 L1525,1335 L1510,1275 L1495,1255 L1175,1255 L1160,1275 L1143,1335 Z"/>
    <path class="die" d="M1057,1320 L1057,742 L1073,718 L1087,658 L1155,658 L1155,620 C1155,510 1510,510 1510,620 L1510,658 L1582,658 L1596,718 L1608,742 L1962,742 L2040,770 L2040,1210 L1962,1237 L1962,1375 C1962,1465 1610,1465 1610,1375 L1610,1320 L1540,1320 L1522,1255 L1510,1237 L1157,1237 L1143,1255 L1127,1320 Z"/>
    <g class="folds" stroke="var(--die)" stroke-width="1.2">
      <line x1="1157" y1="742" x2="1157" y2="1237"/><line x1="1510" y1="742" x2="1510" y2="1237"/>
      <line x1="1608" y1="742" x2="1608" y2="1237"/><line x1="1962" y1="742" x2="1962" y2="1237"/>
      <line x1="1057" y1="742" x2="1962" y2="742"/><line x1="1057" y1="1237" x2="1962" y2="1237"/>
      <line x1="1157" y1="648" x2="1510" y2="648"/><line x1="1610" y1="1330" x2="1962" y2="1330"/>
    </g>
    <path class="safe" d="M1073,1305 L1073,758 L1100,675 L1155,675 M1172,640 C1172,540 1493,540 1493,640 M1510,675 L1568,675 L1592,758 M1625,758 L1962,758 L2024,782 L2024,1198 L1962,1222 M1625,1350 C1625,1445 1945,1445 1945,1350"/>
    <path class="safe" d="M1720,758 C1735,800 1835,800 1850,758"/>

    <!-- top tuck flap -->
    <circle cx="1330" cy="645" r="60" fill="#2a2627"/>
    <g class="suit-row">
      <circle cx="1208" cy="713" r="9" fill="var(--red)"/>
      <circle cx="1250" cy="713" r="2" fill="var(--white)"/>
      <circle cx="1292" cy="713" r="9" fill="var(--green)"/>
      <circle cx="1333" cy="713" r="2" fill="var(--white)"/>
      <path d="M1375,700 L1385,713 L1375,726 L1365,713 Z" fill="var(--gold)"/>
      <circle cx="1416" cy="713" r="2" fill="var(--white)"/>
      <circle cx="1458" cy="713" r="9" fill="var(--purple)"/>
    </g>

    <!-- left spine -->
    <text class="brand-spine" transform="translate(1102,912) rotate(90)">BRAMBLETOYS</text>

    <!-- front panel -->
    <rect x="1163" y="750" width="339" height="480" fill="none" stroke="var(--frame)" stroke-width="2"/>
    <rect x="1175" y="762" width="315" height="456" fill="url(#backPattern)" stroke="#8cc63f" stroke-width="4" stroke-dasharray="2 3" role="img" aria-label="Ornamental card-back pattern with suit corners and circular frame"/>
    <rect x="1185" y="952" width="295" height="76" fill="none" stroke="var(--white)" stroke-width="2"/>
    <text class="front-sub" x="1333" y="920" text-anchor="middle">www.mybrambletoys.co</text>
    <text class="brand-front" x="1333" y="1008" text-anchor="middle" textLength="280" lengthAdjust="spacingAndGlyphs">BRAMBLETOYS</text>
    <text class="front-sub" x="1333" y="1080" text-anchor="middle">PLAYING CARDS</text>
    <path d="M1316,1208 L1350,1208 L1333,1230 Z" fill="var(--ink)" stroke="var(--white)" stroke-width="2"/>

    <!-- right spine -->
    <text class="brand-spine" transform="translate(1566,1040) rotate(-90)">BRAMBLETOYS</text>

    <!-- back panel -->
    <text class="site-url" x="1785" y="838" text-anchor="middle">www.mybrambletoys.com</text>
    <rect x="1720" y="900" width="240" height="330" rx="12" transform="rotate(-20 1840 1065)" fill="url(#backPattern)" stroke="#bbb" stroke-width="1" role="img" aria-label="Tilted ace of spades card illustration"/>

    <!-- bottom flap suits -->
    <g class="suit-row-bottom">
      <circle cx="1688" cy="1287" r="14" fill="var(--purple)"/>
      <circle cx="1716" cy="1287" r="3" fill="var(--white)"/>
      <path d="M1746,1267 L1760,1287 L1746,1307 L1732,1287 Z" fill="var(--gold)"/>
      <circle cx="1777" cy="1287" r="3" fill="var(--white)"/>
      <circle cx="1808" cy="1287" r="14" fill="var(--green)"/>
      <circle cx="1840" cy="1287" r="3" fill="var(--white)"/>
      <circle cx="1872" cy="1287" r="14" fill="var(--red)"/>
    </g>
  </g>
</svg>
</div>
</body>
</html>
```